Copper Fern Photography

Internet sales of landscape photography
Some background on the name.... I'm originally from Kentucky hence the "Copper" and I now live in California wine country, hence the "Fern." The blue coloring in the name is from the Harlow Falcons and the name "photography" is done in a bourbon lettering font. Hope this helps.
Updates
Please include email as dennis@copperfernphotography.com
Please make website www.copperfernphotography.com and ad QR code if possible.
Industry/Entity Type
Landscape
Contact Information for Business Card
Dennis Marlowe
www.copperfernphoto.com
707-555-0192
Requirements
Must have
- My design logo, all contact info :)
I like the thought of a QR Code along with the written link also.

```html
<!DOCTYPE html>
<html lang="en">
<head>
<meta charset="utf-8">
<title>Copper Fern Photography — Business Card</title>
<link rel="stylesheet" href="https://fonts.googleapis.com/css2?family=Exo+2:wght@500;600&display=swap">
<style>
  :root {
    --brand-blue: #1f56a5;
    --ink: #1b1b1b;
    --card-white: #ffffff;
    --backdrop: #ececec;
    --code-tint: #dfe6f1;
  }
  html, body {
    margin: 0;
    padding: 0;
    width: 1200px;
    height: 1000px;
    overflow: hidden;
    background: var(--backdrop);
  }
  .canvas {
    position: relative;
    width: 1200px;
    height: 1000px;
  }
  .business-card {
    position: absolute;
    left: 355px;
    top: 80px;
    width: 490px;
    height: 839px;
    background: var(--card-white);
    box-shadow: 0 2px 10px rgba(0,0,0,0.12);
    font-family: "Exo 2", sans-serif;
    color: var(--brand-blue);
    overflow: hidden;
  }
  .band {
    position: absolute;
    left: 0;
    width: 100%;
    background: var(--brand-blue);
  }
  .band--top { top: 0; height: 27px; }
  .band--bottom { bottom: 0; height: 29px; }
  .wordmark {
    position: absolute;
    left: 0;
    top: 122px;
    width: 100%;
    text-align: center;
    font-weight: 600;
    font-size: 50px;
    line-height: 60px;
    color: var(--brand-blue);
    margin: 0;
  }
  .qr-slot {
    position: absolute;
    left: 180px;
    top: 320px;
    width: 130px;
    height: 130px;
    background: var(--code-tint);
    border: 3px solid var(--brand-blue);
    box-sizing: border-box;
  }
  .holder-name {
    position: absolute;
    left: 47px;
    top: 510px;
    margin: 0;
    font-weight: 500;
    font-size: 72px;
    line-height: 76px;
  }
  .contact-list {
    position: absolute;
    left: 47px;
    top: 672px;
    margin: 0;
    padding: 0;
    list-style: none;
    font-weight: 500;
    font-size: 23px;
    line-height: 35px;
    white-space: nowrap;
  }
  .contact-list li {
    display: flex;
    align-items: center;
    gap: 8px;
  }
  .contact-icon {
    width: 24px;
    height: 24px;
    flex: none;
  }
</style>
</head>
<body>
<main class="canvas">
  <article class="business-card">
    <div class="band band--top"></div>

    <p class="wordmark">Copper Fern<br>Photography</p>

    <div class="qr-slot" role="img" aria-label="QR code linking to www.copperfernphotography.com"></div>

    <h1 class="holder-name">Dennis<br>Marlowe</h1>

    <ul class="contact-list">
      <li>
        <svg class="contact-icon" viewBox="0 0 28 28" aria-hidden="true">
          <g fill="none" stroke="#1b1b1b" stroke-width="2">
            <circle cx="14" cy="14" r="11"/>
            <ellipse cx="14" cy="14" rx="5" ry="11"/>
            <line x1="3" y1="14" x2="25" y2="14"/>
            <line x1="5" y1="8.5" x2="23" y2="8.5"/>
            <line x1="5" y1="19.5" x2="23" y2="19.5"/>
          </g>
        </svg>
        <span>www.copperfernphotography.com</span>
      </li>
      <li>
        <svg class="contact-icon" viewBox="0 0 28 28" aria-hidden="true">
          <g fill="none" stroke="#1b1b1b" stroke-width="2">
            <rect x="3" y="6.5" width="22" height="15" rx="1.5"/>
            <polyline points="3.5,7.5 14,15.5 24.5,7.5"/>
          </g>
        </svg>
        <span>dennis@copperfernphotography.com</span>
      </li>
      <li>
        <svg class="contact-icon" viewBox="0 0 28 28" aria-hidden="true">
          <circle cx="14" cy="14" r="11.5" fill="none" stroke="#1b1b1b" stroke-width="2"/>
          <path d="M10 7.5c-1 .6-2 1.8-1.6 3.6.8 3.6 4.4 7.6 8 8.6 1.6.4 2.8-.4 3.4-1.4l-2.6-2.2-1.6 1.2c-1.8-.8-3.6-2.8-4.2-4.6l1.4-1.4z" fill="#1b1b1b"/>
        </svg>
        <span>707-555-0192</span>
      </li>
    </ul>

    <div class="band band--bottom"></div>
  </article>
</main>
</body>
</html>
```